Young, dynamic furniture company needs a new business card design

We require a new business card design for our modern furniture company which supplies furniture and appliances to the property and development market.
Kestrow Furnishing has become one of the leading furniture & appliance suppliers to the property market withing London. With over 10 years experience, we have increased our business to supply not only private landlords and managing agents, but also property developers, housing associations and local councils.
We offer not only a complete range of furniture which includes beds, wardrobes, dining sets and sofas, but also a high quality, full delivery and assembly service to help you with all our furnishing needs.

Target Market(s)

Private landlords, estate agents, letting agents, property management companies

Industry/Entity Type

Business

Contact Information for Business Card

Name,
Title,
Address,
Mobile,
Telephone,
Fax, Website, email address

Font styles to use
Sans Serif

Colors
3176b5
0555a3
85abd2
cfdeed

Requirements
Must have
• All the above information for each of our staff, along with our logo

```html
<!DOCTYPE html>
<html lang="en">
<head>
<meta charset="utf-8">
<title>Kestrow Furnishing — Business Card</title>
<link href="https://fonts.googleapis.com/css2?family=Montserrat:wght@300;400;500&display=swap" rel="stylesheet">
<style>
  :root {
    --backdrop: #d9d9d9;
    --paper: #f7f7f5;
    --ink: #1b1b1b;
    --brand: #0555a3;
    --brand-mid: #3176b5;
    --muted: #3a3a3a;
  }
  * { box-sizing: border-box; margin: 0; padding: 0; }
  html, body { width: 1200px; height: 900px; overflow: hidden; }
  body {
    background: var(--backdrop);
    font-family: "Montserrat", Arial, sans-serif;
    color: var(--ink);
    position: relative;
  }
  .card {
    position: absolute;
    left: 250px;
    width: 700px;
    height: 400px;
    background: var(--paper);
    box-shadow: 0 6px 18px rgba(0,0,0,0.12);
  }
  .card--front { top: 40px; }
  .card--back { top: 470px; }
  .card__lines { position: absolute; inset: 0; }

  .front-frame {
    position: absolute;
    inset: 22px;
    border: 2px solid var(--ink);
    border-radius: 10px;
  }
  .brand {
    position: absolute;
    left: 0; right: 0; top: 160px;
    display: flex; flex-direction: column; align-items: center;
  }
  .brand__name {
    display: flex; align-items: center; gap: 12px;
    font-weight: 500; font-size: 28px; letter-spacing: 1px;
    color: var(--brand); text-transform: uppercase;
  }
  .brand__mark { width: 22px; height: 22px; background: var(--brand-mid); }
  .brand__tagline {
    margin-top: 8px;
    font-size: 11px; letter-spacing: 2px; font-weight: 400;
    color: var(--muted); text-transform: uppercase;
  }

  .person {
    position: absolute; left: 0; right: 0; top: 112px;
    text-align: center;
  }
  .person__name { font-size: 26px; font-weight: 400; letter-spacing: 2px; text-transform: uppercase; }
  .person__title { font-size: 13px; font-weight: 300; letter-spacing: 3px; text-transform: uppercase; margin-top: 2px; color: var(--muted); }

  .contact {
    position: absolute; top: 238px; width: 190px;
    text-align: center; font-size: 14px; line-height: 1.5; font-weight: 400;
  }
  .contact--phone { left: 40px; }
  .contact--web { left: 255px; }
  .contact--address { left: 470px; }
</style>
</head>
<body>

  <section class="card card--front" aria-label="Card front">
    <div class="front-frame"></div>
    <div class="brand">
      <div class="brand__name"><span class="brand__mark"></span>Kestrow Furnishing</div>
      <div class="brand__tagline">Trade Furniture Solutions</div>
    </div>
  </section>

  <section class="card card--back" aria-label="Card back">
    <svg class="card__lines" width="700" height="400" viewBox="0 0 700 400" fill="none" stroke="#1b1b1b" stroke-width="2" stroke-linejoin="round">
      <path d="M30 30 Q30 20 40 20 H660 Q670 20 670 30 V170 H30 Z"/>
      <path d="M30 85 H338 L350 98 L362 85 H670"/>
      <g fill="#1b1b1b" stroke="none">
        <circle cx="350" cy="62" r="6"/>
        <path d="M339 80 Q339 70 350 70 Q361 70 361 80 Z"/>
      </g>
      <path d="M35 195 H123 L135 208 L147 195 H235 V362 Q235 372 225 372 H45 Q35 372 35 362 Z"/>
      <path d="M250 195 H338 L350 208 L362 195 H450 V362 Q450 372 440 372 H260 Q250 372 250 362 Z"/>
      <path d="M465 195 H553 L565 208 L577 195 H665 V362 Q665 372 655 372 H475 Q465 372 465 362 Z"/>
      <path d="M128 215 q-2 8 8 17 l3 -3 l-4 -4 l-2 2 q-3 -3 -4 -6 l2 -2 l-3 -4 z" fill="#1b1b1b" stroke="none"/>
      <g stroke-width="1.4">
        <circle cx="350" cy="224" r="8"/>
        <ellipse cx="350" cy="224" rx="3.5" ry="8"/>
        <path d="M342 224 H358 M343.5 220 H356.5 M343.5 228 H356.5"/>
      </g>
      <path d="M565 234 Q557 224 557 219 A8 8 0 0 1 573 219 Q573 224 565 234 Z" fill="#1b1b1b" stroke="none"/>
      <circle cx="565" cy="219" r="3" fill="#f7f7f5" stroke="none"/>
    </svg>

    <div class="person">
      <div class="person__name">Daniel Hart</div>
      <div class="person__title">Director</div>
    </div>

    <div class="contact contact--phone">020 7946 0321<br>020 7946 0322<br>020 7946 0323</div>
    <div class="contact contact--web">daniel@kestrow.co<br>www.kestrow.co</div>
    <div class="contact contact--address">14 Marlow Yard<br>London E2 7QT</div>
  </section>

</body>
</html>
```